Aviation security consulting company needs a website

We need a website design for Brisk Holloway, and aviation security consulting company. Brisk Holloway (www.briskholloway.example) is an aviation security consulting company that works with government and industry stakeholders in over 60 countries on aviation security strategy, governance, and oversight at the regulatory and operational level.
Brisk Holloway is strongly internationally focused.
The website required should be simple, corporate, serious, and communicate professionalism, reliability and honesty. We are trying to give the company a feeling of being well established.
The attached files include the company logo, along with examples of company web page styles that we like.
The Brisk Holloway website need only be around five pages long (landing page, who we are, our services, our clients, contact), though don't feel limited to only five pages.
The existing website (www.briskholloway.example) was rushed and put together using Wix. We don't love the existing website as it looks too amateur, so don't use it as a template.
There is no requirement for any online sales tools to be included in the site. The site is purely informational, with the option of people making contact via email.

```html
<!DOCTYPE html>
<html lang="en">
<head>
<meta charset="utf-8">
<title>Brisk Holloway – Aviation Security Consulting</title>
<link href="https://fonts.googleapis.com/css2?family=Roboto:wght@300;400;500;700&display=swap" rel="stylesheet">
<style>
  :root {
    --navy: #1b2a5e;
    --ink: #16203f;
    --text-grey: #555a60;
    --icon-grey: #7a7e83;
    --line: #e4e4e4;
    --white: #ffffff;
    --page-bg: #f7f7f7;
    --hero-top: #8c8a55;
    --hero-mid: #4d5a48;
    --hero-low: #2c3530;
    --arrow-bg: #f2f2f2;
  }
  * { box-sizing: border-box; margin: 0; padding: 0; }
  html, body { width: 1200px; height: 557px; overflow: hidden; }
  body { font-family: "Roboto", Arial, sans-serif; background: var(--page-bg); position: relative; }

  .top-bar { height: 28px; background: var(--white); border-bottom: 1px solid var(--line); position: relative; }
  .social-list { position: absolute; left: 117px; top: 0; display: flex; height: 28px; }
  .social-item { width: 29px; height: 28px; border-left: 1px solid var(--line); display: flex; align-items: center; justify-content: center; font-size: 9px; font-weight: 500; color: var(--icon-grey); line-height: 1; }
  .social-item:last-child { border-right: 1px solid var(--line); }
  .contact-line { position: absolute; right: 117px; top: 0; height: 28px; padding: 0 9px; border-left: 1px solid var(--line); border-right: 1px solid var(--line); font-size: 11px; color: var(--text-grey); line-height: 28px; }

  .site-header { height: 76px; background: var(--white); position: relative; }
  .brand { position: absolute; left: 117px; top: 12px; display: flex; align-items: center; }
  .brand-square { width: 52px; height: 52px; background: var(--navy); margin-right: 8px; }
  .brand-name { font-size: 26px; font-weight: 700; color: var(--ink); line-height: 1; letter-spacing: -0.3px; }
  .brand-tagline { font-size: 11.5px; color: var(--ink); letter-spacing: 1.6px; margin-top: 2px; }
  .main-nav { position: absolute; right: 117px; top: 0; height: 76px; display: flex; align-items: center; gap: 21px; }
  .nav-link { font-size: 11.5px; color: #6b6f74; text-transform: uppercase; letter-spacing: 0.2px; }
  .nav-link.is-active { color: var(--navy); }
  .search-icon { width: 13px; height: 13px; }

  .hero { position: absolute; left: 0; top: 104px; width: 1200px; height: 412px; overflow: hidden; }
  .hero-photo { position: absolute; inset: 0;
    background:
      radial-gradient(ellipse 40% 35% at 47% 20%, rgba(220,220,200,0.55), transparent 70%),
      linear-gradient(180deg, var(--hero-top) 0%, #7c7e52 30%, var(--hero-mid) 60%, var(--hero-low) 100%); }
  .hero-shade { position: absolute; inset: 0; background: linear-gradient(90deg, rgba(0,0,0,0.28), rgba(0,0,0,0.05) 55%, rgba(0,0,0,0.25)); }
  .hero-copy { position: absolute; left: 117px; top: 140px; color: var(--white); }
  .hero-title { font-size: 40px; font-weight: 400; letter-spacing: 0.3px; line-height: 1; }
  .hero-subtitle { font-size: 17px; font-weight: 300; margin-top: 14px; }
  .hero-button { display: inline-block; margin-top: 20px; width: 93px; height: 31px; background: var(--navy); color: var(--white); font-size: 11.5px; font-weight: 500; text-align: center; line-height: 31px; border-radius: 2px; }
  .slider-arrow { position: absolute; top: 181px; width: 35px; height: 35px; display: flex; align-items: center; justify-content: center; }
  .slider-arrow.prev { left: 0; background: var(--arrow-bg); }
  .slider-arrow.next { right: 0; background: rgba(60,64,60,0.7); }
  .slider-dots { position: absolute; left: 584px; top: 384px; display: flex; gap: 6px; }
  .slider-dot { width: 6px; height: 6px; border-radius: 50%; background: rgba(255,255,255,0.45); }
  .slider-dot.is-current { background: var(--white); }
</style>
</head>
<body>
  <div class="top-bar">
    <div class="social-list">
      <span class="social-item">Kite</span>
      <span class="social-item">Orb</span>
      <span class="social-item">Pal</span>
      <span class="social-item">Pix</span>
      <span class="social-item">Dot</span>
    </div>
    <div class="contact-line">Contact us: +1 555 010 0199</div>
  </div>

  <header class="site-header">
    <div class="brand">
      <span class="brand-square"></span>
      <div>
        <div class="brand-name">Brisk Holloway</div>
        <div class="brand-tagline">aviation security consulting</div>
      </div>
    </div>
    <nav class="main-nav">
      <span class="nav-link is-active">Home</span>
      <span class="nav-link">Who We Are</span>
      <span class="nav-link">Our Services</span>
      <span class="nav-link">Our Clients</span>
      <span class="nav-link">Contact Us</span>
      <svg class="search-icon" viewBox="0 0 14 14"><circle cx="6" cy="6" r="4.3" fill="none" stroke="#6b6f74" stroke-width="1.8"/><line x1="9.2" y1="9.2" x2="13" y2="13" stroke="#6b6f74" stroke-width="2" stroke-linecap="round"/></svg>
    </nav>
  </header>

  <section class="hero">
    <div class="hero-photo" role="img" aria-label="Airport departure lounge with rows of seats in front of a large window, an airliner parked outside at sunset"></div>
    <div class="hero-shade"></div>
    <div class="hero-copy">
      <h1 class="hero-title">BRISK HOLLOWAY</h1>
      <p class="hero-subtitle">Aviation Security Consulting</p>
      <span class="hero-button">Learn More..</span>
    </div>
    <span class="slider-arrow prev"><svg width="8" height="10" viewBox="0 0 8 10"><polyline points="5,2 2,5 5,8" fill="none" stroke="#555" stroke-width="1.3"/></svg></span>
    <span class="slider-arrow next"><svg width="8" height="10" viewBox="0 0 8 10"><polyline points="3,2 6,5 3,8" fill="none" stroke="#9a9a9a" stroke-width="1.3"/></svg></span>
    <div class="slider-dots">
      <span class="slider-dot is-current"></span>
      <span class="slider-dot"></span>
      <span class="slider-dot"></span>
    </div>
  </section>
</body>
</html>
```